Flyer für  Bund für lebendige Bürgerwerkstätten
Flyer für Bund für lebendige Bürgerwerkstätten
Zielgruppe
Der Bund für lebendige Bürgerwerkstätten e.V. führt überparteiliche politische Bildungsarbeit für unterschiedliche Zielgruppen durch. Mit diesem Flyer bewerben wir unsere Angebote für Grundschüler:innen. Der Flyer richtet sich also an Lehrkräfte und andere Pädagogische Fachkräfte, die mit Kindern dieser Altersgruppe arbeiten.
Aufgabenstellung
Ich benötige den Flyer in einem horizontalen DIN A4 Format. Der Flyer wird letztlich als Broschüre durch drei gefaltet, sodass es auf der Innen- und Außenseite jeweils 3 Spalten gibt. Der Text befindet sich im Anhang, das Layout entspricht der gewünschten Aufteilung. Unsere Schriftart ist ITC Officina Sans. Die Schriftdatei ist beigefügt.
Das Farbkonzept sollte in Blau- und Grüntönen gehalten sein. Die hex-Codes der Corporate Farben sind #e4003a und #6b7f98. Es sind Bilder beigefügt, Die verwendet und verändert werden dürfen. Es müssen nicht alle Bilder verwendet werden. Die Auswahl obliegt Dir. Bilder müssen auch nicht im Vordergrund stehen, sondern können auch im Hintergrund eingebettet werden. Wir waren uns intern uneinig darüber, ob eine Mischung aus Fotos und Grafiken funktioniert oder „inkonsistent“ wirkt. Triff die Auswahl hier gerne entsprechend Deiner Expertise.
Der angehängte QR-Code muss neben dem Absatz „Wie holen wir den Mitredetag an unsere Schule“ eingefügt werden.
Wichtig ist, dass der Flyer auf der Vorderseite (Spalte 3) und Rückseite (Spalte 2) unser b.l.b.-Logo enthält. Auf der Rückseite müssen unten die Logos der Förderer eingefügt werden. Der hier einzufügende Halbsatz ist im Text-Dokument benannt.

```html
<!DOCTYPE html>
<html lang="de">
<head>
<meta charset="utf-8">
<title>Flyer – Bund für lebendige Bürgerwerkstätten</title>
<link href="https://fonts.googleapis.com/css2?family=Fira+Sans+Condensed:wght@500;600;700&display=swap" rel="stylesheet">
<style>
  :root {
    --brand-red: #e4003a;
    --brand-slate: #6b7f98;
    --text-light: #ffffff;
    --art-mint: #cfe8e4;
    --art-leaf: #dfe8c4;
    --art-blue: #2b3b95;
    --art-gold: #b9cc6a;
  }
  * { box-sizing: border-box; margin: 0; padding: 0; }
  html, body { width: 1200px; height: 848px; overflow: hidden; }
  body {
    position: relative;
    background: var(--brand-red);
    font-family: "Fira Sans Condensed", "Arial Narrow", sans-serif;
    font-weight: 600;
    color: var(--text-light);
  }
  .panel { position: absolute; background: var(--brand-slate); }
  .panel--intro { left: 0; top: 0; width: 368px; height: 809px; border-radius: 0 0 24px 0; }
  .panel--rights { left: 402px; top: 24px; width: 385px; height: 414px; border-radius: 30px; }
  .panel--planet { left: 402px; top: 459px; width: 385px; height: 372px; border-radius: 30px; }
  .panel--democracy { left: 834px; top: 58px; width: 366px; height: 279px; border-radius: 30px 0 0 30px; }
  .panel--europe { left: 840px; top: 358px; width: 360px; height: 279px; border-radius: 30px 0 0 30px; }

  .art { position: absolute; }
  .art--human-rights { left: 42px; top: 384px; width: 307px; height: 191px; border-radius: 24px;
    background: linear-gradient(120deg, var(--art-mint) 0%, #d7ece8 55%, #f3c9b8 100%); }
  .art--kids-globe { left: 555px; top: 6px; width: 245px; height: 204px; border-radius: 30px;
    background: radial-gradient(circle at 50% 75%, #8fcf8a 0%, #7bbde0 28%, #ffffff 52%); }
  .art--sustainability { left: 575px; top: 446px; width: 225px; height: 187px; border-radius: 30px;
    background: radial-gradient(circle at 50% 50%, #ffffff 40%, var(--art-leaf) 100%); }
  .art--megaphone { left: 1074px; top: 0; width: 126px; height: 110px; border-radius: 0 0 0 60px;
    background: linear-gradient(160deg, var(--art-gold) 0%, #e1b85a 60%, rgba(228,0,58,0) 100%); }
  .art--eu-flag { left: 1119px; top: 504px; width: 81px; height: 117px; border-radius: 6px 0 0 6px;
    background: linear-gradient(180deg, var(--art-blue) 0%, var(--art-blue) 60%, #f2c4a6 100%); }

  .heading {
    position: absolute;
    font-weight: 700;
    text-transform: uppercase;
    letter-spacing: 0.03em;
    white-space: nowrap;
  }
  .heading--lg { font-size: 22.5px; line-height: 29px; }
  .heading--md { font-size: 19.5px; line-height: 23.4px; }
  .copy {
    position: absolute;
    font-size: 14px;
    line-height: 21.5px;
    letter-spacing: 0.025em;
    white-space: nowrap;
  }
</style>
</head>
<body>

  <section class="panel panel--intro" aria-label="Einleitung"></section>
  <h1 class="heading heading--lg" style="left:42px; top:68px;">Politische Bildung in<br>der Grundschule</h1>
  <div class="copy" style="left:42px; top:128px;">
    Kinder begegnen täglich politischen Themen: Sie<br>
    stellen Fragen, verhandeln, diskutieren Regeln.<br>
    Werte wie Gerechtigkeit, Respekt und<br>
    Menschenrechte spielen dabei eine wichtige Rolle.<br>
    Unsere Mitredetage knüpfen daran an und machen<br>
    Politik altersgerecht erlebbar.<br>
    <br>
    Wir möchten:<br>
    – Interesse an politischen Themen wecken<br>
    – Kinder stärken, eigene Standpunkte zu entwickeln<br>
    – ein Gefühl für globale Verantwortung fördern
  </div>
  <div class="art art--human-rights" role="img" aria-label="Illustration: übereinandergelegte Hände mit Schriftzug Human Rights"></div>

  <h2 class="heading heading--lg" style="left:42px; top:607px;">Wer ist der B.L.B.?</h2>
  <div class="copy" style="left:42px; top:638px;">
    Der Bund für lebendige Bürgerwerkstätten<br>
    organisiert seit über 30 Jahren überparteiliche<br>
    Bildungsangebote für junge Menschen – von<br>
    Projekttagen an Schulen bis zu Seminaren in<br>
    Deutschland und Europa.
  </div>

  <section class="panel panel--rights" aria-label="Kinderrechte"></section>
  <div class="art art--kids-globe" role="img" aria-label="Illustration: Kinder stehen Hand in Hand hinter einer Weltkugel in den Wolken"></div>
  <h2 class="heading heading--md" style="left:416px; top:124px;">Meine Rechte,<br>deine Rechte –<br>Kinderrechte<br>entdecken</h2>
  <div class="copy" style="left:413px; top:224px;">
    Kinder lernen spielerisch, welche Rechte sie haben –<br>
    zum Beispiel auf Bildung, Gesundheit und freie<br>
    Meinungsäußerung.<br>
    Anhand der Reise eines Kleidungsstücks entlang der<br>
    Lieferkette wird deutlich, wo Kinderrechte weltweit<br>
    berührt werden.<br>
    Geschichten von engagierten Kindern zeigen:<br>
    Auch ihre Stimme zählt.
  </div>

  <section class="panel panel--planet" aria-label="Nachhaltigkeit"></section>
  <div class="art art--sustainability" role="img" aria-label="Illustration: Weltkugel mit Keimling, Recycling-Symbol und Glühbirne zwischen Blättern"></div>
  <h2 class="heading heading--md" style="left:412px; top:540px;">Nur noch kurz<br>die Welt retten –<br>Nachhaltigkeit<br>im Alltag</h2>
  <div class="copy" style="left:415px; top:647px;">
    In diesem Programm entdecken Kinder, wie sie im Alltag<br>
    nachhaltiger handeln können: beim Einkaufen, beim<br>
    Umgang mit Energie und beim Verbrauch von<br>
    Ressourcen. Mit Geschichten, Spielen und kleinen<br>
    Aktionen erfahren sie, was fairer Handel bedeutet und<br>
    wie sie selbst die Umwelt schützen können.<br>
    &nbsp;So erleben sie: Ihr Handeln macht einen Unterschied.
  </div>

  <section class="panel panel--democracy" aria-label="Demokratie"></section>
  <div class="art art--megaphone" role="img" aria-label="Illustration: Megafon mit Sprechblasen"></div>
  <h2 class="heading heading--md" style="left:857px; top:101px;">Wer ist hier der Bestimmer? –<br>Demokratie erleben</h2>
  <div class="copy" style="left:857px; top:155px;">
    Wie fühlt es sich an, mitbestimmen zu dürfen?<br>
    &nbsp;In spielerischen Übungen lernen Kinder, ihre<br>
    Meinung zu äußern, gemeinsam<br>
    Entscheidungen zu treffen und Verantwortung<br>
    zu übernehmen.<br>
    &nbsp;So wird Demokratie nicht nur erklärt, sondern<br>
    direkt erlebt.
  </div>

  <section class="panel panel--europe" aria-label="Europa"></section>
  <h2 class="heading heading--md" style="left:865px; top:383px;">Europa entdecken! – Die EU im<br>Alltag der Kinder</h2>
  <div class="copy" style="left:865px; top:434px;">
    Mit Puzzles, Bastelaktionen und kleinen<br>
    Experimenten erkunden wir, was die<br>
    Europäische Union ist und welche Rolle sie im<br>
    Alltag der Kinder spielt.<br>
    &nbsp;Themen wie Reisefreiheit, gemeinsame<br>
    Währung und kulturelle Vielfalt werden<br>
    anschaulich und kindgerecht vermittelt.
  </div>
  <div class="art art--eu-flag" role="img" aria-label="Illustration: Hand hält eine Europaflagge"></div>

  <h2 class="heading heading--md" style="left:865px; top:700px;">Nichts Passendes dabei?</h2>
  <div class="copy" style="left:865px; top:728px;">
    Wir entwickeln Projekttage gerne gemeinsam<br>
    mit Ihnen weiter und passen Themen flexibel<br>
    an den Bedarf Ihrer Schule an.
  </div>

</body>
</html>
```